Valbrook Data Works

Our company is about IT hardwares and IT solutions. IT hardware such as PC, RAMS, storage and servers. IT solutions such as project management, BA. We are also selling new technology too.

Target Market(s)

Consumer, Small to Medium Business, Corporate

Requirements
Must have
• The business card must have the following:
• Name:
• Title:
• Contact Number:
• Email address:
• Website:
• Color: Must match the logo color upgrade

```html
<!DOCTYPE html>
<html lang="en">
<head>
<meta charset="utf-8">
<title>Valbrook Data Works – Business Card</title>
<link href="https://fonts.googleapis.com/css2?family=Montserrat:wght@400;500;700;800&display=swap" rel="stylesheet">
<style>
  :root {
    --page: #ececec;
    --card-light: #ffffff;
    --card-dark: #2b2a29;
    --card-dark-edge: #353433;
    --ink: #3a3a3a;
    --ink-soft: #555555;
    --accent: #c8822f;
    --rule: #cfcfcf;
    --on-dark: #f2f2f2;
  }
  * { box-sizing: border-box; margin: 0; padding: 0; }
  html, body { width: 1200px; height: 1147px; overflow: hidden; }
  body {
    background: var(--page);
    font-family: "Montserrat", sans-serif;
    display: flex;
    flex-direction: column;
    align-items: center;
    justify-content: center;
    gap: 60px;
  }
  .card {
    width: 880px;
    height: 503px;
    position: relative;
    box-shadow: 0 6px 20px rgba(0,0,0,0.12);
  }

  /* Front */
  .card--front {
    background: var(--card-light);
    display: flex;
    align-items: center;
  }
  .brand {
    width: 50%;
    display: flex;
    align-items: center;
    justify-content: center;
    gap: 16px;
  }
  .brand__mark {
    width: 22px; height: 22px;
    background: var(--accent);
  }
  .brand__name {
    font-weight: 800;
    font-size: 30px;
    letter-spacing: 1px;
    color: var(--ink);
    text-transform: uppercase;
    line-height: 1.15;
  }
  .divider {
    width: 1px;
    height: 190px;
    background: var(--rule);
  }
  .contact {
    padding-left: 50px;
    color: var(--ink-soft);
    font-size: 17px;
    line-height: 1.5;
  }
  .contact__name {
    color: var(--accent);
    font-weight: 800;
    font-size: 22px;
    text-transform: uppercase;
    letter-spacing: 0.5px;
  }
  .contact__title { margin-bottom: 8px; }
  .contact__address { margin-bottom: 8px; }
  .contact__line { display: flex; align-items: center; gap: 10px; }
  .contact__line svg { width: 16px; height: 16px; flex: none; }

  /* Back */
  .card--back {
    background: var(--card-dark);
    display: flex;
    align-items: center;
    justify-content: center;
    overflow: hidden;
  }
  .back__pattern {
    position: absolute;
    inset: 0;
    background: radial-gradient(circle at 50% 45%, var(--card-dark-edge), var(--card-dark) 70%);
  }
  .back__content {
    position: relative;
    text-align: center;
  }
  .back__brand {
    display: flex;
    align-items: center;
    gap: 16px;
    justify-content: center;
  }
  .back__brand .brand__name { color: var(--on-dark); font-size: 36px; }
  .back__web {
    margin-top: 26px;
    color: var(--on-dark);
    font-size: 17px;
    letter-spacing: 0.5px;
  }
</style>
</head>
<body>

  <section class="card card--front">
    <div class="brand">
      <span class="brand__mark"></span>
      <span class="brand__name">Valbrook<br>Data Works</span>
    </div>
    <div class="divider"></div>
    <div class="contact">
      <p class="contact__name">Daniel Hartley</p>
      <p class="contact__title">Managing Director</p>
      <p class="contact__address">Kerkstraat 48<br>9050 Ledeberg</p>
      <p class="contact__line">
        <svg viewBox="0 0 16 16"><path d="M4 1.5l2.5 3-1.5 1.5c.8 1.8 2.2 3.2 4 4l1.5-1.5 3 2.5-1.5 2.5C7 13 3 9 1.5 3.5z" fill="none" stroke="#c8822f" stroke-width="1.4" stroke-linejoin="round"/></svg>
        +32 470 55 18 20
      </p>
      <p class="contact__line">
        <svg viewBox="0 0 16 16"><rect x="1.5" y="3.5" width="13" height="9" fill="none" stroke="#c8822f" stroke-width="1.4"/><path d="M1.5 3.5l6.5 5 6.5-5" fill="none" stroke="#c8822f" stroke-width="1.4"/></svg>
        daniel@valbrookdata.com
      </p>
      <p class="contact__line">
        <svg viewBox="0 0 16 16"><circle cx="8" cy="8" r="6.5" fill="none" stroke="#c8822f" stroke-width="1.4"/><ellipse cx="8" cy="8" rx="2.8" ry="6.5" fill="none" stroke="#c8822f" stroke-width="1.2"/><path d="M1.5 8h13" stroke="#c8822f" stroke-width="1.2"/></svg>
        www.valbrookdata.com
      </p>
    </div>
  </section>

  <section class="card card--back">
    <div class="back__pattern" role="img" aria-label="Faint network pattern of thin connected lines and nodes"></div>
    <div class="back__content">
      <div class="back__brand">
        <span class="brand__mark"></span>
        <span class="brand__name">Valbrook Data Works</span>
      </div>
      <p class="back__web">www.valbrookdata.com</p>
    </div>
  </section>

</body>
</html>
```